Electronic hardware design and manufacturer needing a new business card design.

We need a new business card design consisting of a double sided design adhering to brand and logo guidelines attached. I also want to incorporate something that recognizes our 25th year in business ("EST 2001" or something like that....).

Need extra days to review

Need extra days to review

```html
<!DOCTYPE html>
<html lang="en">
<head>
<meta charset="utf-8">
<title>Northline Circuit Works – Business Card</title>
<link href="https://fonts.googleapis.com/css2?family=Montserrat:wght@400;500;700;800&display=swap" rel="stylesheet">
<style>
  :root {
    --stage: #2b2b2d;
    --card-dark: #05060c;
    --streak: #1f3a8a;
    --navy: #123a5a;
    --ink: #1c2530;
    --muted: #3d4753;
    --paper: #ffffff;
    --pale: #e8eef4;
    --orange: #f5a11c;
    --red: #d7261e;
  }
  * { box-sizing: border-box; margin: 0; padding: 0; }
  html, body { width: 1200px; height: 875px; overflow: hidden; }
  body {
    background: var(--stage);
    font-family: "Montserrat", sans-serif;
    position: relative;
  }
  .card {
    position: absolute;
    width: 525px;
    height: 300px;
    border-radius: 18px;
    overflow: hidden;
    box-shadow: 0 18px 40px rgba(0,0,0,.45);
  }
  /* Front side */
  .card--front {
    left: 70px; top: 120px;
    background: var(--card-dark);
  }
  .card--front .glow {
    position: absolute; inset: 0;
    background:
      radial-gradient(ellipse 60% 18% at 72% 42%, rgba(60,100,220,.55), transparent 70%),
      linear-gradient(160deg, #0a0d1c 0%, var(--card-dark) 60%);
  }
  .card--front .brand {
    position: absolute; left: 0; right: 0; top: 50%;
    transform: translateY(-50%);
    text-align: center;
    color: var(--pale);
  }
  .brand__mark {
    display: inline-flex; align-items: center; gap: 14px;
    font-weight: 800; font-size: 64px; letter-spacing: 2px;
  }
  .brand__mark .dot {
    width: 22px; height: 22px; background: var(--orange);
  }
  .brand__name {
    margin-top: 6px;
    font-weight: 700; font-size: 13px; letter-spacing: 3px;
  }
  /* Back side */
  .card--back {
    left: 605px; top: 455px;
    background: var(--paper);
  }
  .card--back .logo {
    position: absolute; left: 38px; top: 40px;
    color: var(--navy);
  }
  .logo__mark { font-weight: 800; font-size: 78px; line-height: .9; letter-spacing: 2px; }
  .logo__name { font-weight: 800; font-size: 12.5px; letter-spacing: 2.2px; margin-top: 6px; }
  .person {
    position: absolute; left: 38px; top: 178px;
    width: 200px; text-align: right;
  }
  .person__name { font-weight: 700; font-size: 22px; color: var(--ink); }
  .person__title { font-weight: 400; font-size: 12px; color: var(--muted); margin-top: 2px; }
  .divider {
    position: absolute; left: 256px; top: 158px;
    width: 1px; height: 78px; background: var(--ink);
  }
  .contacts {
    position: absolute; left: 272px; top: 160px;
    list-style: none; font-size: 12px; color: var(--ink);
  }
  .contacts li { display: flex; align-items: center; gap: 8px; height: 24px; }
  .contacts svg { width: 12px; height: 12px; flex: none; }
  .footer-line {
    position: absolute; left: 0; right: 0; bottom: 26px;
    text-align: center; font-size: 12px; color: var(--ink);
  }
</style>
</head>
<body>

  <section class="card card--front" aria-label="Card front">
    <div class="glow" role="img" aria-label="Dark background with a soft blue light streak"></div>
    <div class="brand">
      <div class="brand__mark"><span>NCW</span><span class="dot"></span></div>
      <div class="brand__name">NORTHLINE CIRCUIT WORKS</div>
    </div>
  </section>

  <section class="card card--back" aria-label="Card back">
    <div class="logo">
      <div class="logo__mark">NCW</div>
      <div class="logo__name">NORTHLINE CIRCUIT WORKS</div>
    </div>

    <div class="person">
      <div class="person__name">Daniel Reyes</div>
      <div class="person__title">Managing Director</div>
    </div>

    <div class="divider"></div>

    <ul class="contacts">
      <li>
        <svg viewBox="0 0 12 12" aria-hidden="true"><path d="M2.5 1 L4.5 1 L5.2 3.6 L4 4.6 Q5 7 7.4 8 L8.4 6.8 L11 7.5 L11 9.5 Q10.5 11 9 11 Q1 10 1 3 Q1 1.5 2.5 1Z" fill="var(--orange)"/></svg>
        555-014-0199
      </li>
      <li>
        <svg viewBox="0 0 12 12" aria-hidden="true"><rect x="0.5" y="2.5" width="11" height="7" fill="var(--navy)"/><path d="M0.5 2.5 L6 6.5 L11.5 2.5" stroke="#fff" stroke-width="1" fill="none"/></svg>
        info@northlinecircuit.ca
      </li>
      <li>
        <svg viewBox="0 0 12 12" aria-hidden="true"><circle cx="6" cy="6" r="5.5" fill="var(--red)"/><path d="M0.5 6 H11.5 M6 0.5 Q3 6 6 11.5 M6 0.5 Q9 6 6 11.5" stroke="#fff" stroke-width=".8" fill="none"/></svg>
        www.northlinecircuit.ca
      </li>
    </ul>

    <div class="footer-line">Northline Circuit Works | EST. 2001</div>
  </section>

</body>
</html>
```